Harbourlight Campus Lodgings needs a business card design

Hi Guys,

We are a Student Accommodation company in Australia. We already have a logo which I will submit.

I will require the design of the business cards from you.

I am after something that looks clean, modern and that people feel interested and actually want to contact us.

We would like to see designs that are innovative.

On the business cards I will require to have:

Employee Name
Position
Phone number
Email
Facebook page

I hope you can help me with this project guys as I have heard really good things from you.

```html
<!DOCTYPE html>
<html lang="en">
<head>
<meta charset="utf-8">
<title>Harbourlight Campus Lodgings – Business Card</title>
<link rel="stylesheet" href="https://fonts.googleapis.com/css2?family=Oswald:wght@600&family=Jura:wght@500;600&family=Open+Sans:wght@400&display=swap">
<style>
  :root {
    --backdrop: #c9ced6;
    --card-white: #fafafa;
    --card-grey: #e6e6e6;
    --brand-green: #1f9a1f;
    --brand-yellow: #f0b323;
    --ink-dark: #3b3b3b;
    --ink-on-green: #0f5f12;
  }
  * { box-sizing: border-box; margin: 0; padding: 0; }
  html, body { width: 1200px; height: 866px; overflow: hidden; }
  body { background: var(--backdrop); position: relative; font-family: "Jura", sans-serif; }

  .card {
    position: absolute;
    width: 560px;
    height: 320px;
    overflow: hidden;
    box-shadow: 0 8px 22px rgba(0,0,0,0.18);
  }
  .card-front {
    left: 80px; top: 80px;
    background: radial-gradient(circle at 45% 45%, #ffffff 0%, var(--card-white) 55%, var(--card-grey) 100%);
    display: flex; align-items: center; justify-content: center;
  }
  .card-back {
    left: 560px; top: 466px;
    background: linear-gradient(160deg, #ffffff 0%, var(--card-white) 45%, var(--card-grey) 100%);
  }

  .brand { display: flex; align-items: center; gap: 12px; }
  .brand-square { width: 46px; height: 46px; background: var(--brand-yellow); flex: none; }
  .brand-name {
    font-family: "Oswald", sans-serif; font-weight: 600;
    color: var(--brand-green); text-transform: uppercase;
    line-height: 1.05; font-size: 24px; letter-spacing: 0.5px;
  }
  .card-back .brand { position: absolute; left: 28px; top: 48px; gap: 9px; }
  .card-back .brand-square { width: 30px; height: 30px; }
  .card-back .brand-name { font-size: 15px; }

  .back-shapes { position: absolute; inset: 0; }

  .holder { position: absolute; right: 28px; top: 42px; text-align: right; color: var(--ink-dark); }
  .holder-name { font-weight: 600; font-size: 18px; letter-spacing: 1.5px; }
  .holder-role { font-family: "Open Sans", sans-serif; font-size: 11px; margin-top: 2px; }

  .address { position: absolute; right: 28px; top: 150px; text-align: right; color: var(--ink-on-green); font-size: 11.5px; line-height: 1.5; }
  .website { position: absolute; right: 28px; top: 216px; color: var(--ink-on-green); font-size: 11.5px; }

  .contacts { position: absolute; left: 26px; bottom: 18px; list-style: none; color: var(--ink-on-green); font-size: 11px; }
  .contacts li { display: flex; align-items: center; gap: 8px; height: 17px; }
  .contacts svg { width: 11px; height: 11px; fill: var(--ink-on-green); flex: none; }
</style>
</head>
<body>

  <section class="card card-front">
    <div class="brand">
      <span class="brand-square"></span>
      <span class="brand-name">Harbourlight<br>Campus<br>Lodgings</span>
    </div>
  </section>

  <section class="card card-back">
    <svg class="back-shapes" viewBox="0 0 560 320" preserveAspectRatio="none">
      <path d="M0,238 C210,236 390,160 560,84 L560,320 L0,320 Z" fill="var(--brand-green)"/>
      <path d="M0,214 C200,208 360,150 470,104 C370,156 210,226 0,236 Z" fill="var(--brand-yellow)"/>
    </svg>

    <div class="brand">
      <span class="brand-square"></span>
      <span class="brand-name">Harbourlight<br>Campus<br>Lodgings</span>
    </div>

    <div class="holder">
      <p class="holder-name">DANIEL WHITFORD</p>
      <p class="holder-role">Managing Director</p>
    </div>

    <p class="address">214 9th floor,Quay<br>Harbour Road NSW</p>
    <p class="website">www.hclodgings.com</p>

    <ul class="contacts">
      <li><svg viewBox="0 0 12 12"><path d="M2,0.5 L4.2,0.5 L5,3.2 L3.6,4.3 C4.3,5.8 5.6,7.2 7.3,8 L8.4,6.7 L11.3,7.5 L11.3,9.8 C11.3,10.8 10.5,11.4 9.6,11.3 C4.7,10.7 1.1,7 0.6,2.2 C0.5,1.2 1.1,0.5 2,0.5 Z"/></svg>021 555 0143</li>
      <li><svg viewBox="0 0 12 12"><path d="M3,0 H9 V12 H3 Z M4,1.5 V9.5 H8 V1.5 Z M5.5,10.3 H6.5 V11.2 H5.5 Z"/></svg>021 555 0143</li>
      <li><svg viewBox="0 0 12 12"><path d="M3,0 H8 V3.5 H3 Z M1,4 H11 V10 H1 Z M3,7.5 H9 V12 H3 Z"/></svg>021 555 0143</li>
      <li><svg viewBox="0 0 12 12"><path d="M0.5,2 H11.5 V10 H0.5 Z M1.5,3 L6,6.6 L10.5,3 Z" fill-rule="evenodd"/></svg>dan@hclodge.com</li>
    </ul>
  </section>

</body>
</html>
```